International Life Insurer Needs a Web Design

What We Do: We are a boutique financial services firm specializing in solutions that financial services professionals can integrate into comprehensive wealth preservation strategies for their clients. Strategies we provide may run the spectrum from simple life insurance products to complex cases with very sophisticated and intricate solutions.

Industry Type: Financial & Insurance

Top Things to Communicate Through Our Web Design:
#1 Ultra High Net Worth
#2 INTERNATIONAL
#3 Private Banking
#4 Expertise
________________________________________
Our Target Audience:
Financial institutions/private banks who have high net worth/ultra high net worth international clients looking for unparalleled expertise in wealth preservation, taxation, and business insurance. The audience is the financial service professional, not the end client of the financial services. We will direct the professional to the site.
We Like These Designs. (fonts, colors, style):
Simple font, clean, modern, contemporary, blue colors
NOT stodgy, old, gothic, etc.

Secondarily, we’d like to also create a small tri-fold brochure incorporating the web elements (design, text), so the ability to transfer the design to print might be a plus.

Project Deadline Extended
Reason: to allow for additional design work

Target Market(s)

Financial services professionals catering to their ultra high net worth clients

Industry/Entity Type

Life Insurance

Requirements
Must have
• Our logo (see uploaded file)
Nice to have
• the existing website includes some text that could be reviewed for ideas and incorporated into the design: http://marlowcrestadvisory.example/

```html
<!DOCTYPE html>
<html lang="en">
<head>
<meta charset="utf-8">
<title>Marlowcrest Advisory Group — Home</title>
<link href="https://fonts.googleapis.com/css2?family=Arimo:wght@400;700&family=Cormorant+Garamond:wght@500&display=swap" rel="stylesheet">
<style>
:root{
  --navy:#1d3e8a;
  --band-top:#0a4486;
  --band-bottom:#0b5db8;
  --link:#1aa0d8;
  --title:#22a6dc;
  --text:#444;
  --muted-bg:#f4f4f4;
  --line:#d9d9d9;
  --heading:#4c5878;
  --btn:#4d5b7d;
}
*{box-sizing:border-box;margin:0;padding:0}
html,body{width:1200px;height:1015px;overflow:hidden;background:#fff;font-family:"Arimo",Arial,sans-serif;color:var(--text)}
.page{position:relative;width:1200px;height:1015px}
.abs{position:absolute}

.brand{left:157px;top:13px;display:flex;align-items:center;gap:8px}
.brand-mark{width:60px;height:60px;background:var(--navy)}
.brand-name{font-size:24px;line-height:22px;color:var(--navy);letter-spacing:-0.5px}

.search-field{left:655px;top:39px;width:281px;height:28px;border:2px solid #bbb;border-top-color:#888;background:#fff}
.search-btn{left:945px;top:39px;width:104px;height:28px;background:linear-gradient(#66739a,var(--btn));border-radius:3px;color:#fff;font-size:16px;text-align:center;line-height:28px}

.nav{left:0;top:90px;width:1200px;height:38px;background:var(--muted-bg)}
.nav-item{position:absolute;top:11px;font-size:17px;color:var(--link)}

.band{left:0;top:128px;width:1200px;height:372px;background:linear-gradient(var(--band-top),var(--band-bottom))}
.card{left:130px;top:152px;width:940px;height:610px;background:#fff;box-shadow:0 8px 20px rgba(0,0,0,.05)}

.dropdown{left:223px;top:128px;width:190px;height:88px;background:#f4f4f4;border-bottom:3px solid #ddd}
.dropdown-hover{left:223px;top:128px;width:190px;height:24px;background:#c8d4e2}
.drop-item{position:absolute;left:235px;font-size:17px;color:var(--link)}

.page-title{left:159px;top:188px;font-family:"Cormorant Garamond",Georgia,serif;font-size:32px;color:var(--title)}

.main-box{left:154px;top:236px;width:585px;height:452px;border:1px solid var(--line);background:#fff}
.main-photo{left:493px;top:236px;width:246px;height:118px;background:linear-gradient(90deg,#fff 0%,#e7e8ec 35%,#9aa3b6 70%,#2f3c5c 100%)}
.main-copy{left:169px;top:270px;width:520px;font-size:15px;line-height:17.6px}
.main-copy p{margin-bottom:17px}
.main-copy .intro{width:285px;margin-bottom:18px}
.main-copy .point{margin-bottom:17.5px}

.tab{left:771px;top:236px;width:126px;height:35px;border:1px solid var(--line);border-bottom:none;background:#fff;font-size:16px;font-weight:700;color:#444;padding:10px 0 0 12px}
.side-list{left:771px;top:269px;width:264px;height:419px;border:1px solid var(--line)}
.side-item{height:69px;border-bottom:1px solid #e2e2e2;display:flex;padding:12px 0 0 10px;gap:8px}
.side-item:nth-child(even){background:#f6f6f6}
.side-item:last-child{border-bottom:none}
.thumb{width:66px;height:48px;flex:none}
.side-text{font-size:11.4px;font-weight:700;line-height:12.8px;color:#444;width:175px}

.footer{left:0;top:762px;width:1200px;height:205px;background:var(--muted-bg);border-top:1px solid #ddd}
.footer-heading{position:absolute;font-family:"Cormorant Garamond",Georgia,serif;font-size:31px;color:var(--heading)}
.social{position:absolute;top:75px;width:52px;height:52px;border-radius:50%;box-shadow:0 3px 4px rgba(0,0,0,.25);border:2px solid #fff}
.footer-copy{position:absolute;left:508px;top:63px;width:545px;font-size:15px;line-height:18px;color:#444}

.legal{right:125px;top:979px;display:flex;gap:21px;font-size:9.5px;color:#333}
</style>
</head>
<body>
<div class="page">
  <div class="abs brand">
    <div class="brand-mark"></div>
    <div class="brand-name">Marlowcrest<br>Advisory Group</div>
  </div>
  <div class="abs search-field"></div>
  <div class="abs search-btn">Search</div>

  <div class="abs nav">
    <span class="nav-item" style="left:159px">Home</span>
    <span class="nav-item" style="left:225px">About Us</span>
    <span class="nav-item" style="left:312px">Case Studies</span>
    <span class="nav-item" style="left:434px">Solutions for Deverse Needs</span>
  </div>

  <div class="abs band"></div>
  <div class="abs card"></div>

  <div class="abs page-title">Home</div>

  <div class="abs dropdown"></div>
  <div class="abs dropdown-hover"></div>
  <span class="drop-item" style="top:133px">Our History</span>
  <span class="drop-item" style="top:157px">Our Niche</span>
  <span class="drop-item" style="top:182px">Our Value Proposition</span>

  <div class="abs main-box"></div>
  <div class="abs main-photo" role="img" aria-label="Photo of hands reviewing financial charts with a pen"></div>
  <div class="abs main-copy">
    <p class="intro">At Marlowcrest Advisory Group, protecting your clients’ families, their businesses, and their lifestyles are at the forefront of all we do.</p>
    <p class="point">· Unsurpassed service, support, and underwriting</p>
    <p class="point">· Licensed to conduct business nationally</p>
    <p class="point">· Advising businesses and families for over 50 years</p>
    <p class="point">· Independent, objective, and resourceful</p>
    <p>There are many advantages to working with Marlowcrest Advisory Group. We offer the service and attention of a boutique agency, while leveraging the strength of preeminent American and offshore life insurance companies.</p>
    <p>In addition, since we are privately owned we base our actions and recommendations on what is best for our clients without regard to stockholder profit or share price.</p>
  </div>

  <div class="abs tab">Some Heading</div>
  <div class="abs side-list">
    <div class="side-item"><div class="thumb" role="img" aria-label="Photo of a tall tower at dusk" style="background:linear-gradient(#c9ccd1,#4a4d55)"></div><div class="side-text">Proin gravida nibh vel velit auctor aliquet. Aenean sollicitudin, lorem quis</div></div>
    <div class="side-item"><div class="thumb" role="img" aria-label="Photo of a red rose" style="background:linear-gradient(135deg,#c8a070,#b9473a,#e9dcc6)"></div><div class="side-text">Aenean sollicitudin, lorem quis bibendum auctor, nisi elit consequat ipsum, nec sagittis</div></div>
    <div class="side-item"><div class="thumb" role="img" aria-label="Photo of glass skyscrapers against the sky" style="background:linear-gradient(#a9c2e0,#5b7399 60%,#3b5b2a)"></div><div class="side-text">Sem nibh id elit. Duis sed odio sit amet nibh vulputate cursus a sit amet mauris.</div></div>
    <div class="side-item"><div class="thumb" role="img" aria-label="Photo of a music player and earphones" style="background:linear-gradient(135deg,#eee,#777 60%,#222)"></div><div class="side-text">Cursus a sit amet mauris. accumsan ipsum velit. Nam nec tellus a odio tincidunt</div></div>
    <div class="side-item"><div class="thumb" role="img" aria-label="Photo of a small toy figure on a globe" style="background:linear-gradient(#1a2333,#5a4a3a 70%,#8a8a3a)"></div><div class="side-text">Nam nec tellus a odio tincidunt auctor.ornare odio. Sed non mauris vitae erat consequat.</div></div>
    <div class="side-item"><div class="thumb" role="img" aria-label="Photo of a coffee cup and notes on a desk" style="background:linear-gradient(135deg,#555,#bbb 55%,#eee)"></div><div class="side-text">Sed non mauris vitae erat consequat. auctor eu in elit. Class aptent taciti sociosqu.</div></div>
  </div>

  <div class="abs footer">
    <div class="footer-heading" style="left:160px;top:14px">Find us on</div>
    <div class="social" style="left:152px;background:#2b5aa8" aria-label="Social profile"></div>
    <div class="social" style="left:208px;background:#7fd0f0" aria-label="Social profile"></div>
    <div class="social" style="left:264px;background:#17607a" aria-label="Social profile"></div>
    <div class="social" style="left:320px;background:#d8d8dc" aria-label="Social profile"></div>
    <div class="footer-heading" style="left:507px;top:14px">Some Heading</div>
    <div class="footer-copy">Proin gravida nibh vel velit auctor aliquet. Aenean sollicitudin, lorem quis bibendum auctor, nisi elit consequat ipsum, nec sagittis sem nibh id elit. Duis sed odio sit amet nibh vulputate cursus a sit amet mauris. Morbi accumsan ipsum . consequat ipsum, nec sagittis sem nibh id elit.</div>
  </div>

  <div class="abs legal">
    <span>FAQs</span><span>Contact Us</span><span>Terms &amp; conditions</span><span>Privacy policy</span>
  </div>
</div>
</body>
</html>
```